Business Card Design

We need a design for business cards for our company. We have a logo. We teach EMT's and we are based out of Virginia. The information that will need to add would be, name, title, phone number, email, address. On the back of the business card would be "We Train You, To Save Lives"

Target Market(s)

People that want to become EMT's

Colors

Designer to choose colors to be used in the design.

Requirements
Must have
• company logo

```html
<!DOCTYPE html>
<html lang="en">
<head>
<meta charset="utf-8">
<title>RescueTrain Co – Business Card</title>
<link rel="stylesheet" href="https://fonts.googleapis.com/css2?family=Arimo:wght@400;700&display=swap">
<style>
  :root {
    --slate: #3f4a55;
    --paper: #f7f7f7;
    --pink: #ee3d5c;
    --ink: #2b2f33;
    --grey: #b9bfc5;
    --bg: #e6e6e6;
  }
  * { box-sizing: border-box; margin: 0; padding: 0; }
  html, body { width: 1200px; height: 800px; overflow: hidden; }
  body {
    background: var(--bg);
    font-family: "Arimo", Arial, sans-serif;
    position: relative;
  }
  .card {
    position: absolute;
    left: 300px;
    width: 600px;
    height: 343px;
    border-radius: 4px;
    overflow: hidden;
    box-shadow: 0 6px 18px rgba(0,0,0,0.18);
    background: var(--slate);
  }
  .card--front { top: 38px; }
  .card--back { top: 419px; }

  .brand {
    display: flex;
    align-items: center;
    gap: 9px;
    color: var(--pink);
    font-weight: 700;
    letter-spacing: 1px;
    text-transform: uppercase;
    white-space: nowrap;
  }
  .brand__dot {
    width: 12px; height: 12px;
    border-radius: 50%;
    background: var(--pink);
    flex: none;
  }
  .card--front .brand {
    position: absolute;
    left: 0; top: 170px;
    width: 330px;
    justify-content: center;
    font-size: 22px;
  }

  .info-panel {
    position: absolute;
    left: 330px; top: 0;
    width: 270px; height: 343px;
    background: var(--paper);
  }
  .info-panel__bar {
    position: absolute;
    left: 0; top: 58px;
    width: 7px; height: 285px;
    background: var(--pink);
  }
  .person {
    position: absolute;
    left: 44px; top: 62px;
    padding-left: 12px;
    border-left: 4px solid var(--pink);
    color: var(--ink);
  }
  .person__name { font-size: 23px; line-height: 1.05; }
  .person__name span { color: var(--pink); }
  .person__title { font-size: 20px; line-height: 1.15; }

  .contacts {
    position: absolute;
    left: 44px; top: 150px;
    list-style: none;
    color: var(--ink);
    font-size: 14.5px;
  }
  .contacts li {
    display: flex;
    align-items: flex-start;
    gap: 10px;
    margin-bottom: 9px;
    line-height: 1.25;
  }
  .contacts svg { flex: none; width: 15px; height: 15px; margin-top: 1px; fill: var(--pink); }

  .card--back .brand {
    position: absolute;
    left: 0; right: 0; top: 128px;
    justify-content: center;
    font-size: 38px;
  }
  .tagline {
    position: absolute;
    left: 0; right: 0; top: 192px;
    text-align: center;
    color: var(--grey);
    font-size: 21px;
  }
</style>
</head>
<body>

<section class="card card--front">
  <div class="brand"><span class="brand__dot"></span>RescueTrain Co</div>

  <div class="info-panel">
    <div class="info-panel__bar"></div>
    <div class="person">
      <p class="person__name">Daniel <span>Hart</span></p>
      <p class="person__title">Director</p>
    </div>
    <ul class="contacts">
      <li>
        <svg viewBox="0 0 16 16" aria-hidden="true"><path d="M4 1h3l1 4-2 1.5a9 9 0 0 0 3.5 3.5L11 8l4 1v3c0 1-1 2-2 2C7 14 2 9 2 3c0-1 1-2 2-2z"/></svg>
        <span>0522 44 67890</span>
      </li>
      <li>
        <svg viewBox="0 0 16 16" aria-hidden="true"><path d="M1 3h14v10H1z M1.5 3.5 8 9l6.5-5.5" stroke="#f7f7f7" stroke-width="1.2"/></svg>
        <span>hello@rescuetrainco.com</span>
      </li>
      <li>
        <svg viewBox="0 0 16 16" aria-hidden="true"><circle cx="8" cy="8" r="7"/><path d="M1 8h14M8 1c3 3 3 11 0 14M8 1c-3 3-3 11 0 14" stroke="#f7f7f7" stroke-width="1" fill="none"/></svg>
        <span>www.rescuetrainco.com</span>
      </li>
      <li>
        <svg viewBox="0 0 16 16" aria-hidden="true"><path d="M8 1a5 5 0 0 1 5 5c0 4-5 9-5 9S3 10 3 6a5 5 0 0 1 5-5z"/><circle cx="8" cy="6" r="2" fill="#f7f7f7"/></svg>
        <span>2204/56 harbour road,<br>riverton qld 4100</span>
      </li>
    </ul>
  </div>
</section>

<section class="card card--back">
  <div class="brand"><span class="brand__dot"></span>RescueTrain Co</div>
  <p class="tagline">We Train You, To Save Lives</p>
</section>

</body>
</html>
```